Aerial Photography Business Card Design

I am looking for a business card for my drone photography business.

Contents should include
Back:
preferably a design involving one or more image(s) I have attached

OR logo and background of designer's choice

Front:
Tom Halvick
Aerial Photography
Real Estate, Construction, Inspection
FAA Certified Drone Pilot
Please include a simple logo for drone business.

Phone: 5185550147

Format should be .psd or .ai
please also include a copy as .pdf format.

```html
<!DOCTYPE html>
<html lang="en">
<head>
<meta charset="utf-8">
<title>Kestrel Photography – Business Card</title>
<link href="https://fonts.googleapis.com/css2?family=Lato:wght@400;700&display=swap" rel="stylesheet">
<style>
  :root {
    --page-bg: #1c1f22;
    --card-dark: #03181b;
    --card-teal: #0b4a52;
    --accent-blue: #2aa6e6;
    --text-light: #e8eef0;
    --text-blue: #33aee8;
    --frame-black: #061012;
    --badge-teal: #0d5a63;
    --photo-sky: #8fb3cf;
    --photo-green: #5e7d4a;
    --photo-roof: #b9a89a;
    --photo-city: #8b6e5c;
  }
  * { margin: 0; padding: 0; box-sizing: border-box; }
  html, body { width: 1200px; height: 900px; overflow: hidden; }
  body {
    background: var(--page-bg);
    font-family: "Lato", sans-serif;
    display: flex;
    align-items: center;
    justify-content: center;
    gap: 40px;
  }
  .card {
    width: 540px;
    height: 309px;
    border-radius: 6px;
    position: relative;
    overflow: hidden;
    box-shadow: 0 10px 30px rgba(0,0,0,.5);
  }

  /* Front */
  .card-front {
    background: radial-gradient(ellipse at 35% 35%, var(--card-teal) 0%, var(--card-dark) 70%);
    color: var(--text-light);
  }
  .brand {
    position: absolute;
    left: 40px;
    top: 60px;
    display: flex;
    align-items: center;
    gap: 12px;
  }
  .brand-dot {
    width: 30px; height: 30px;
    border-radius: 50%;
    background: var(--accent-blue);
  }
  .brand-name {
    font-weight: 700;
    color: var(--text-blue);
    font-size: 22px;
    line-height: 1.05;
    letter-spacing: 1px;
    text-transform: uppercase;
  }
  .details {
    position: absolute;
    left: 270px;
    top: 70px;
    width: 240px;
  }
  .person-name {
    color: var(--text-blue);
    font-size: 22px;
    font-weight: 400;
  }
  .person-role { font-size: 12px; margin-top: 2px; }
  .services { font-size: 11.5px; margin-top: 12px; line-height: 1.35; }
  .divider {
    height: 1px;
    background: var(--accent-blue);
    margin: 14px 0 12px;
    width: 220px;
  }
  .contact-list { list-style: none; font-size: 13px; }
  .contact-list li { display: flex; align-items: center; gap: 8px; margin-bottom: 6px; }
  .contact-list svg { width: 13px; height: 13px; fill: var(--text-light); flex: none; }

  /* Back */
  .card-back {
    background: var(--frame-black);
    padding: 16px;
  }
  .corner { position: absolute; width: 70px; height: 40px; border: 5px solid var(--accent-blue); }
  .corner-tl { top: 0; left: 0; border-right: none; border-bottom: none; border-top-left-radius: 6px; }
  .corner-tr { top: 0; right: 0; border-left: none; border-bottom: none; border-top-right-radius: 6px; }
  .corner-bl { bottom: 0; left: 0; border-right: none; border-top: none; border-bottom-left-radius: 6px; }
  .corner-br { bottom: 0; right: 0; border-left: none; border-top: none; border-bottom-right-radius: 6px; }
  .collage {
    width: 100%; height: 100%;
    display: grid;
    grid-template-columns: 1fr 1fr 1fr;
    grid-template-rows: 1fr 1fr 1fr;
    gap: 3px;
    border-radius: 8px;
    overflow: hidden;
    position: relative;
  }
  .photo { width: 100%; height: 100%; }
  .photo-campus { background: linear-gradient(160deg, var(--photo-sky), var(--photo-green)); }
  .photo-lake { background: linear-gradient(180deg, #9fb8c8, #3d6f9a); }
  .photo-city { background: linear-gradient(170deg, #b7c2cc, var(--photo-city)); }
  .photo-house-pink { background: linear-gradient(170deg, #c9a9a0, var(--photo-green)); }
  .photo-house-white { background: linear-gradient(170deg, var(--photo-roof), #6d8a58); }
  .photo-cathedral { background: linear-gradient(170deg, #c4c8c2, #8a7c62); }
  .photo-yard { background: linear-gradient(170deg, #8fa57a, #47603a); }
  .photo-villa { background: linear-gradient(170deg, #cfd6dc, #56774a); }
  .photo-river { background: linear-gradient(170deg, #7c9a6a, #4f6b45); }
  .back-badge {
    position: absolute;
    left: 50%; top: 50%;
    transform: translate(-50%, -50%);
    background: var(--badge-teal);
    padding: 20px 24px;
    display: flex;
    align-items: center;
    gap: 10px;
  }
  .back-badge .brand-name { color: var(--accent-blue); font-size: 17px; }
  .back-badge .brand-dot { width: 22px; height: 22px; }
</style>
</head>
<body>
  <section class="card card-front" aria-label="Business card front">
    <div class="brand">
      <span class="brand-dot"></span>
      <span class="brand-name">Kestrel<br>Photography</span>
    </div>
    <div class="details">
      <h1 class="person-name">Tom Halvick</h1>
      <p class="person-role">Aerial Photography</p>
      <p class="services">Real Estate, Construction, Inspection<br>FAA Certified Drone Pilot</p>
      <div class="divider"></div>
      <ul class="contact-list">
        <li>
          <svg viewBox="0 0 24 24" aria-hidden="true"><path d="M6.6 10.8a15.1 15.1 0 0 0 6.6 6.6l2.2-2.2c.3-.3.7-.4 1-.2 1.1.4 2.3.6 3.6.6.6 0 1 .4 1 1V20c0 .6-.4 1-1 1C10.6 21 3 13.4 3 4c0-.6.4-1 1-1h3.5c.6 0 1 .4 1 1 0 1.3.2 2.5.6 3.6.1.3 0 .7-.2 1z"/></svg>
          5185550147
        </li>
        <li>
          <svg viewBox="0 0 24 24" aria-hidden="true"><path d="M2 5h20v14H2zm2 2v.5l8 5 8-5V7zm0 2.8V17h16V9.8l-8 5z"/></svg>
          tom@kestrelphotography.com
        </li>
        <li>
          <svg viewBox="0 0 24 24" aria-hidden="true"><path d="M12 2a10 10 0 1 0 0 20 10 10 0 0 0 0-20zm6.9 6h-3a15 15 0 0 0-1.3-3.9A8 8 0 0 1 18.9 8zM12 4c.8 1.1 1.5 2.5 1.9 4h-3.8c.4-1.5 1.1-2.9 1.9-4zM4.3 14a8 8 0 0 1 0-4h3.4a16 16 0 0 0 0 4zm.8 2h3a15 15 0 0 0 1.3 3.9A8 8 0 0 1 5.1 16zm3-8h-3a8 8 0 0 1 4.3-3.9C8.8 5.3 8.4 6.6 8.1 8zM12 20c-.8-1.1-1.5-2.5-1.9-4h3.8c-.4 1.5-1.1 2.9-1.9 4zm2.3-6H9.7a14 14 0 0 1 0-4h4.6a14 14 0 0 1 0 4zm.3 5.9c.6-1.2 1-2.5 1.3-3.9h3a8 8 0 0 1-4.3 3.9zM16.3 14a16 16 0 0 0 0-4h3.4a8 8 0 0 1 0 4z"/></svg>
          www.kestrelphotography.com
        </li>
      </ul>
    </div>
  </section>

  <section class="card card-back" aria-label="Business card back">
    <span class="corner corner-tl"></span>
    <span class="corner corner-tr"></span>
    <span class="corner corner-bl"></span>
    <span class="corner corner-br"></span>
    <div class="collage">
      <div class="photo photo-campus" role="img" aria-label="Aerial photo of a ring-shaped campus building"></div>
      <div class="photo photo-lake" role="img" aria-label="Aerial photo of a mountain lake"></div>
      <div class="photo photo-city" role="img" aria-label="Aerial photo of a city skyline"></div>
      <div class="photo photo-house-pink" role="img" aria-label="Aerial photo of a residential home with garden"></div>
      <div class="photo photo-house-white" role="img" aria-label="Aerial photo of a white-roofed house"></div>
      <div class="photo photo-cathedral" role="img" aria-label="Aerial photo of a cathedral"></div>
      <div class="photo photo-yard" role="img" aria-label="Aerial photo of a landscaped yard"></div>
      <div class="photo photo-villa" role="img" aria-label="Aerial photo of a villa with pool"></div>
      <div class="photo photo-river" role="img" aria-label="Aerial photo of a river park"></div>
      <div class="back-badge">
        <span class="brand-dot"></span>
        <span class="brand-name">Kestrel<br>Photography</span>
      </div>
    </div>
  </section>
</body>
</html>
```